Corvane Health a direct primary care practice needs a beautiful and customer friendly website

We need a website to showcase our new medical practice. We want to enhance the customer experience and make it easy to navigate to the desired page by placing pillar pages on the home screen. the website needs to be clean and bright.

Target Market(s)

Uninsured, Small businesses that can't afford to offer employees insurance.

Industry/Entity Type

Healthcare

Coding

Coded - Design and coding required

Font styles to use
Serif
Sans Serif

Colors
0592cd
3377b5
0355a3
9bcb3c
acd136

Requirements
Must have
• Must be user friendly, must have pillar pages to help boost SEO ranking, clean and bright, must be close to the in colors to the attached logo.

Content will be very similar to www.brisklomacare.example
Nice to have
• Clean and easy to read font

```html
<!DOCTYPE html>
<html lang="en">
<head>
<meta charset="utf-8">
<title>Corvane Health — Direct Primary Care</title>
<link rel="stylesheet" href="https://fonts.googleapis.com/css2?family=IBM+Plex+Sans:wght@400;500;600;700&display=swap">
<style>
:root{
  --navy:#0e3a5b;
  --ink:#1f2a33;
  --text:#3c4750;
  --green:#8cc63f;
  --blue:#1a7fc1;
  --wave:#1674bb;
  --blush:#f4f0f0;
  --footer:#2b2b2c;
  --line:#d7dde2;
}
*{box-sizing:border-box;margin:0;padding:0}
html,body{width:1200px;height:4135px;overflow:hidden}
body{position:relative;font-family:"IBM Plex Sans",Arial,sans-serif;color:var(--text);background:#fff}
.abs{position:absolute}
.btn{position:absolute;display:flex;align-items:center;justify-content:center;color:#fff;font-weight:600;text-transform:uppercase;letter-spacing:.3px;border:2px solid rgba(255,255,255,.85)}
.btn-green{background:var(--green)}
.btn-blue{background:var(--blue)}
.heading{position:absolute;left:0;width:1200px;text-align:center;color:var(--navy);font-weight:600;font-size:23px;letter-spacing:.3px}
.rule{position:absolute;width:50px;height:2px;background:var(--green)}
.photo{position:absolute}
.wave{position:absolute;left:0;width:1200px}

/* header */
.brand{left:132px;top:44px;font-size:33px;font-weight:600;color:var(--navy);letter-spacing:.5px}
.call{left:582px;top:20px;display:flex;gap:10px;align-items:center}
.call small{display:block;font-size:11px;color:var(--ink)}
.call b{display:block;font-size:18px;font-weight:500;color:var(--ink);letter-spacing:.5px}
.nav{left:432px;top:78px;display:flex;gap:0;font-size:14px;color:var(--ink)}
.nav a{color:inherit;text-decoration:none;margin-right:29px}
.nav a.active{color:var(--blue);text-decoration:underline;font-weight:600}

/* hero */
.hero-title{left:128px;top:248px;font-size:46px;font-weight:700;line-height:53px;color:var(--navy);letter-spacing:1px}
.dots{left:562px;top:622px;display:flex;gap:9px}
.dots i{width:7px;height:7px;border-radius:50%;background:rgba(255,255,255,.8);display:block}
.dots i.on{background:var(--green);box-shadow:0 0 0 2px #fff}

/* services */
.card{position:absolute;top:814px;width:297px;height:341px;border:1.5px solid #7fb3d8;background:#fff;text-align:center}
.card svg{margin-top:30px}
.card h3{margin-top:22px;font-size:15px;font-weight:600;color:var(--ink);letter-spacing:.3px}
.card p{margin:20px auto 0;width:236px;font-size:12.5px;line-height:19px;color:var(--text)}
.card .btn{left:101px;bottom:36px;width:94px;height:29px;font-size:11px}
.arrow{position:absolute;top:972px}

/* welcome */
.welcome-bg{left:0;top:1288px;width:1200px;height:560px;background:var(--blush)}
.kicker{font-size:18px;color:var(--navy);font-weight:500}
.big{font-size:30px;font-weight:700;color:var(--navy);letter-spacing:.5px}
.para{font-size:15px;line-height:24px;color:var(--text)}

/* blog */
.blog-bg{left:0;top:2483px;width:1200px;height:640px;background:var(--blush)}
.post{position:absolute;top:2612px;height:408px;background:#fff;box-shadow:0 2px 8px rgba(0,0,0,.06)}
.post .photo{left:0;top:0;width:100%;height:188px}
.post h4{position:absolute;left:25px;top:214px;font-size:15px;line-height:22px;font-weight:600;color:var(--ink)}
.post p{position:absolute;left:25px;top:269px;width:240px;font-size:12px;line-height:16px;color:var(--text)}
.post .btn{left:25px;top:356px;width:91px;height:27px;font-size:11px}

/* footer */
.footer{left:0;top:3770px;width:1200px;height:365px;background:var(--footer);color:#fff}
.fcol h5{font-size:13px;font-weight:600;letter-spacing:.5px;margin-bottom:22px}
.fmenu li{list-style:none;font-size:12px;line-height:20px;color:#e6e6e6}
.fitem{display:flex;gap:12px;align-items:center;margin-bottom:20px;font-size:12px;line-height:16px;color:#e6e6e6}
.fitem .ic{width:22px;height:22px;border-radius:50%;background:#fff;flex:none;display:flex;align-items:center;justify-content:center}
</style>
</head>
<body>

<!-- header -->
<div class="abs brand">Corvane Health</div>
<div class="abs call">
  <svg width="28" height="28" viewBox="0 0 24 24" fill="none" stroke="#1f2a33" stroke-width="1.6"><path d="M5 3h4l2 5-2.5 1.5a11 11 0 0 0 6 6L16 13l5 2v4a2 2 0 0 1-2 2A17 17 0 0 1 3 5a2 2 0 0 1 2-2z"/><path d="M14 3a7 7 0 0 1 7 7M14 7a3 3 0 0 1 3 3"/></svg>
  <div><small>CALL US</small><b>555.010.4477</b></div>
</div>
<div class="btn btn-green" style="left:766px;top:18px;width:181px;height:37px;font-size:13px">Book Appointment</div>
<div class="btn btn-blue" style="left:960px;top:18px;width:107px;height:37px;font-size:13px">Join Us</div>
<nav class="abs nav">
  <a class="active">HOME</a><a>ABOUT</a><a>SERVICES</a><a>EMPLOYERS</a><a>PRICING</a><a>FAQ</a><a>CONTACT US</a><a style="margin-right:0">BLOG</a>
</nav>

<!-- hero -->
<div class="photo" role="img" aria-label="Smiling young girl in a yellow top being examined by a doctor with a stethoscope in a bright clinic" style="left:0;top:118px;width:1200px;height:612px;background:linear-gradient(90deg,#e9dcd6 0%,#f3e6e2 35%,#eedcc8 55%,#f4efea 75%,#e8e6e4 100%)"></div>
<div class="abs hero-title">EXPECT MORE<br>FROM YOUR<br>DOCTOR</div>
<div class="btn btn-green" style="left:133px;top:434px;width:150px;height:49px;font-size:16px">Read More</div>
<div class="abs dots"><i></i><i></i><i class="on"></i><i></i><i></i></div>
<svg class="wave" style="top:660px" width="1200" height="72" viewBox="0 0 1200 72"><path d="M0 72 L0 70 Q600 -10 1200 70 L1200 72 Z" fill="#fff"/><path d="M0 70 Q600 -10 1200 70" fill="none" stroke="var(--wave)" stroke-width="6"/></svg>

<!-- services -->
<div class="heading" style="top:735px">OUR SERVICES</div>
<div class="rule" style="left:575px;top:777px"></div>

<svg class="arrow" style="left:62px" width="32" height="20" viewBox="0 0 32 20" fill="none" stroke="#555" stroke-width="1.6"><path d="M31 10H2M10 2 2 10l8 8"/></svg>
<svg class="arrow" style="left:1096px" width="32" height="20" viewBox="0 0 32 20" fill="none" stroke="#555" stroke-width="1.6"><path d="M1 10h29M22 2l8 8-8 8"/></svg>

<div class="card" style="left:132px">
  <svg width="80" height="80" viewBox="0 0 80 80" fill="none" stroke="var(--blue)" stroke-width="2.2"><path d="M40 44 24 28a9 9 0 0 1 16-10 9 9 0 0 1 16 10z"/><path d="M40 22v14M33 29h14"/><path d="M6 38l6 20 14 12v6M74 38l-6 20-14 12v6M12 46l10 10 8 2M68 46 58 56l-8 2"/></svg>
  <h3>GENERAL HEALTH VISITS</h3>
  <p>There are many variations of passages of Lorem Ipsum ava ilable, but the majority have suff ered alteration in some form by injected.</p>
  <div class="btn btn-green">Read More</div>
</div>
<div class="card" style="left:452px">
  <svg width="80" height="80" viewBox="0 0 80 80" fill="none" stroke="var(--blue)" stroke-width="2.2"><rect x="12" y="10" width="44" height="62" rx="2"/><rect x="26" y="5" width="16" height="9" rx="2"/><path d="M20 26h6v6h-6zM20 40h6v6h-6zM20 54h6v6h-6zM32 29h14M32 43h10M32 57h8"/><path d="M52 30v14a10 10 0 0 0 20 0"/><circle cx="72" cy="52" r="4"/></svg>
  <h3>DIAGNOSTIC TESTING</h3>
  <p>There are many variations of passages of Lorem Ipsum ava ilable, but the majority have suff ered alteration in some form by injected.</p>
  <div class="btn btn-green">Read More</div>
</div>
<div class="card" style="left:772px">
  <svg width="80" height="80" viewBox="0 0 80 80" fill="none" stroke="var(--blue)" stroke-width="2.2"><rect x="14" y="10" width="46" height="62" rx="2"/><rect x="28" y="5" width="18" height="9" rx="2"/><path d="M37 20v14M30 27h14M22 44h28M22 52h22M22 60h16"/><path d="M66 40 50 66l-4 5 1-6 16-26z"/></svg>
  <h3>PHYSICAL EXAMS</h3>
  <p>There are many variations of passages of Lorem Ipsum ava ilable, but the majority have suff ered alteration in some form by injected.</p>
  <div class="btn btn-green">Read More</div>
</div>
<div class="btn btn-blue" style="left:526px;top:1196px;width:148px;height:35px;font-size:12px">View All Services</div>

<!-- welcome -->
<div class="abs welcome-bg"></div>
<div class="photo" role="img" aria-label="Doctor in a white coat writing notes at a desk in a bright office" style="left:132px;top:1331px;width:448px;height:345px;background:linear-gradient(135deg,#e2e4e3,#cfd3d1 60%,#b9a895)"></div>
<div class="photo" role="img" aria-label="Doctor measuring a patient's blood pressure" style="left:108px;top:1494px;width:236px;height:247px;border:3px solid #fff;background:linear-gradient(135deg,#dfe3e2,#c6cac8 55%,#8d9698)"></div>
<div class="photo" role="img" aria-label="Patient talking with a doctor across a desk" style="left:441px;top:1570px;width:162px;height:187px;border:3px solid #fff;background:linear-gradient(135deg,#e8e8e6,#c9c4be 60%,#7b6a5e)"></div>
<div class="abs kicker" style="left:650px;top:1344px">WELCOME TO</div>
<div class="abs big" style="left:650px;top:1370px">CORVANE HEALTH</div>
<div class="rule" style="left:650px;top:1421px"></div>
<p class="abs para" style="left:652px;top:1455px;width:410px">At vero eos et accusamus et iusto odio dignissimos ducimus qui blanditiis praesentium voluptatum deleniti atque corrupti quos dolores et quas molestias excepturi sint occaecati cupiditate non provident, similique sunt in culpa qui officia deserunt mollitia animi, id est laborum et dolorum fuga. Et harum quidem rerum facilis est et expedita distinctio. Nam libero tempore, cum soluta nobis est eligendi optio cumque nihil impedit.</p>
<div class="btn btn-green" style="left:655px;top:1680px;width:113px;height:36px;font-size:13px">Read More</div>
<svg class="wave" style="top:1780px" width="1200" height="72" viewBox="0 0 1200 72"><path d="M0 72 L0 70 Q600 -10 1200 70 L1200 72 Z" fill="#fff"/><path d="M0 70 Q600 -10 1200 70" fill="none" stroke="var(--wave)" stroke-width="6"/></svg>

<!-- benefits -->
<div class="heading" style="top:1882px">BENEFITS OF OUR PRIMARY CARE CLINIC</div>
<div class="rule" style="left:575px;top:1929px"></div>
<div class="abs" style="left:130px;top:2004px;font-size:15px;line-height:26px;font-weight:600;color:var(--ink)">SED UT PERSPICIATIS UNDE OMNIS<br>ISTE NATUS ERROR SIT</div>
<p class="abs para" style="left:130px;top:2073px;width:330px">At vero eos et accusamus et iusto odio dignissimos ducimus qui blanditiis praes entium voluptatum deleniti atque corrupti quos dolores et quas molestias excepturi sint occaecati cupiditate non provident, similique sunt in culpa qui officia deserunt mollitia animi, id est laborum et dolorum fuga. Et harum quidem rerum facilis est et expedita distinctio. Nam libero tempore, cum soluta nobis est eligendi optio cumque nihil impedit.</p>
<div class="btn btn-green" style="left:131px;top:2368px;width:113px;height:37px;font-size:13px">Read More</div>
<div class="photo" role="img" aria-label="Little girl holding a teddy bear while a doctor listens with a stethoscope" style="left:494px;top:1990px;width:575px;height:419px;background:linear-gradient(120deg,#f1f1ef,#e3e4e2 45%,#b8c2cc 70%,#d9c7b6)"></div>

<!-- blog -->
<div class="abs blog-bg"></div>
<div class="heading" style="top:2521px">LATEST BLOG</div>
<div class="rule" style="left:575px;top:2567px"></div>

<div class="post" style="left:132px;width:297px">
  <div class="photo" role="img" aria-label="Doctor examining a young boy with a stethoscope" style="background:linear-gradient(135deg,#eef0ee,#d2d9d6 55%,#7c9a7a)"></div>
  <h4>SED UT PERSPICIATIS UNDE<br>ISTE NATUS ERROR SIT</h4>
  <p>At vero eos et accusamus et iusto odio dignissimos ducimus qui blanditiis praes entium voluptatum deleniti atque corrupti quos dolores</p>
  <div class="btn btn-green">Read More</div>
</div>
<div class="post" style="left:449px;width:297px">
  <div class="photo" role="img" aria-label="Team of doctors reviewing results at a desk" style="background:linear-gradient(135deg,#e6e7e6,#c8cccd 55%,#6f7d8b)"></div>
  <h4>SED UT PERSPICIATIS UNDE<br>ISTE NATUS ERROR SIT</h4>
  <p>At vero eos et accusamus et iusto odio dignissimos ducimus qui blanditiis praes entium voluptatum deleniti atque corrupti quos dolores</p>
  <div class="btn btn-green">Read More</div>
</div>
<div class="post" style="left:771px;width:297px">
  <div class="photo" role="img" aria-label="Doctor consulting with a male patient at a clinic desk" style="background:linear-gradient(135deg,#e8ebed,#c3ccd3 50%,#3f5f86)"></div>
  <h4>SED UT PERSPICIATIS UNDE<br>ISTE NATUS ERROR SIT</h4>
  <p>At vero eos et accusamus et iusto odio dignissimos ducimus qui blanditiis praes entium voluptatum deleniti atque corrupti quos dolores</p>
  <div class="btn btn-green">Read More</div>
</div>
<svg class="wave" style="top:3056px" width="1200" height="72" viewBox="0 0 1200 72"><path d="M0 72 L0 70 Q600 -10 1200 70 L1200 72 Z" fill="#fff"/><path d="M0 70 Q600 -10 1200 70" fill="none" stroke="var(--wave)" stroke-width="6"/></svg>

<!-- personal care -->
<div class="photo" role="img" aria-label="Smiling doctor with glasses checking a young girl's heartbeat with a red stethoscope" style="left:132px;top:3178px;width:566px;height:512px;background:linear-gradient(120deg,#f2f2f2,#e6e6e4 45%,#d6cec6 70%,#efe9e4)"></div>
<div class="abs" style="left:600px;top:3225px;width:470px;height:420px;background:#fff"></div>
<div class="abs" style="left:630px;top:3262px;font-size:23px;line-height:34px;font-weight:700;color:var(--navy);letter-spacing:.4px">ENJOY MORE PERSONAL MEDICAL<br>CARE IN HUNTINGTON BEACH</div>
<div class="rule" style="left:633px;top:3336px"></div>
<p class="abs para" style="left:636px;top:3362px;width:420px">At vero eos et accusamus et iusto odio dignissimos ducimus qui blanditiis praes entium voluptatum deleniti atque corrupti quos dolores et quas molestias excepturi sint occaecati cupiditate non provident, similique sunt in culpa qui officia deserunt mollitia animi, id est laborum et dolorum fuga. Et harum quidem rerum facilis est et expedita distinctio. Nam libero tempore, cum soluta nobis est eligendi optio cumque nihil impedit.</p>
<div class="btn btn-green" style="left:640px;top:3579px;width:113px;height:36px;font-size:13px">Read More</div>

<!-- footer -->
<svg class="wave" style="top:3728px" width="1200" height="50" viewBox="0 0 1200 50"><path d="M0 50 L0 44 Q600 -14 1200 44 L1200 50 Z" fill="var(--footer)"/><path d="M0 44 Q600 -14 1200 44" fill="none" stroke="var(--wave)" stroke-width="6"/></svg>
<footer class="abs footer">
  <div class="abs" style="left:132px;top:140px;font-size:34px;font-weight:600;color:#fff;letter-spacing:.5px">Corvane Health</div>

  <div class="abs fcol" style="left:532px;top:67px">
    <h5>MENU</h5>
    <ul class="fmenu"><li>HOME</li><li>ABOUT</li><li>SERVICES</li><li>EMPLOYERS</li><li>PRICING</li><li>FAQ</li><li>CONTACT US</li><li>BLOG</li></ul>
  </div>

  <div class="abs fcol" style="left:696px;top:67px">
    <h5>CONTACT US</h5>
    <div class="fitem"><span class="ic"><svg width="10" height="12" viewBox="0 0 10 12"><path d="M5 0a4 4 0 0 1 4 4c0 3-4 8-4 8S1 7 1 4a4 4 0 0 1 4-4z" fill="#2b2b2c"/><circle cx="5" cy="4" r="1.5" fill="#fff"/></svg></span><span>2261 Alder Crest Road<br>Linmoor, CA 90000</span></div>
    <div class="fitem"><span class="ic"><svg width="11" height="11" viewBox="0 0 24 24"><path d="M5 3h4l2 5-2.5 1.5a11 11 0 0 0 6 6L16 13l5 2v4a2 2 0 0 1-2 2A17 17 0 0 1 3 5a2 2 0 0 1 2-2z" fill="#2b2b2c"/></svg></span><span>Call Us<br>555.010.4477</span></div>
    <div class="fitem"><span class="ic"><svg width="11" height="9" viewBox="0 0 12 9"><rect width="12" height="9" rx="1" fill="#2b2b2c"/><path d="M0 1l6 4 6-4" stroke="#fff" fill="none"/></svg></span><span>E mail Us<br>info@corvanehealth.example</span></div>
  </div>

  <div class="abs fcol" style="left:958px;top:67px">
    <h5>FOLLOW US</h5>
    <div class="fitem"><span class="ic"></span><span>Like us on<br>PULSEBOARD</span></div>
    <div class="fitem"><span class="ic"></span><span>Follow us on<br>CHIRPLY</span></div>
    <div class="fitem"><span class="ic"></span><span>Follow us on<br>WORKLOOP</span></div>
  </div>

  <div class="abs" style="left:132px;top:285px;width:936px;height:1px;background:#4a4a4b"></div>
  <div class="abs" style="left:0;top:327px;width:1200px;text-align:center;font-size:10px;color:#cfcfcf">Copyright © 2021 All Rights Reserved</div>
</footer>

</body>
</html>
```